Hearthside Living Partners postcard

Hearthside Living Partners ®Our mission is to help our client’s to continue living in their own homes safely, independently, and comfortably as they age. Our team is comprised of Certified Aging in Place specialists, Universal Design Consultants, Registered Nurses and Certified Home Inspectors. We utilize our skills and training to assess, design and optimize our client’s homes to handle whatever physical challenges the future may bring, allowing them to remain where they want to be as they age…..at home!New company! We need a postcard for a direct mail campaign to help us launch. We understand all of the copy included in the attached document may not fit on the postcard. Demo is 55+ I know what you are thinking, where is the log? We don't have one. Long story short, in the past we have spent WAY too much time and EFFORT milling over a logo. SO...this time we found a font within Microsoft Word and applied it to our name and like it. Take a look at the uploaded document. Feel free to play with it a little...

Target Market(s)

55+ with a slight slant toward females viewer.

Font styles to use
Serif

Colors
85acd3
0355a3
ffffff

Requirements
Must have
• 1. statistics section-grab their attention
• 2. our mission statement- the goal
Nice to have
• 1. How we can help section
• Senior Services Industry

```html
<!DOCTYPE html>
<html lang="en">
<head>
<meta charset="utf-8">
<title>Hearthside Living Partners – Postcard</title>
<link rel="stylesheet" href="https://fonts.googleapis.com/css2?family=Lato:ital,wght@0,400;0,700;0,900;1,400;1,700&family=Roboto+Condensed:wght@400&display=swap">
<style>
  :root {
    --blue-deep: #0355a3;
    --blue-mid: #2a74c0;
    --blue-light: #85acd3;
    --blue-pale: #a9c6e4;
    --white: #ffffff;
    --ink: #1c1c1c;
    --ink-soft: #2b2b2b;
    --backdrop: #a27448;
    --photo-a: #c9d3d6;
    --photo-b: #e6d7c7;
  }
  * { box-sizing: border-box; margin: 0; padding: 0; }
  html, body { width: 907px; height: 1200px; overflow: hidden; }
  body {
    background: var(--backdrop);
    font-family: "Lato", sans-serif;
    position: relative;
  }

  .card {
    position: absolute;
    left: 135px;
    width: 657px;
    height: 509px;
    overflow: hidden;
    box-shadow: 0 3px 10px rgba(0,0,0,.35);
  }

  /* ---------- Front ---------- */
  .card-front {
    top: 47px;
    background: linear-gradient(160deg, var(--blue-mid) 0%, var(--blue-deep) 60%, #0a5db0 100%);
  }
  .front-topband {
    position: absolute; left: 0; top: 0; width: 335px; height: 25px;
    background: linear-gradient(90deg, var(--blue-light), var(--blue-pale));
  }
  .front-left {
    position: absolute; left: 0; top: 25px; width: 335px; height: 442px;
    background: var(--white);
  }
  .brand {
    text-align: center; padding-top: 4px;
  }
  .brand-name {
    font-family: "Lato", sans-serif; font-weight: 700; font-size: 22px;
    color: var(--blue-deep); letter-spacing: -.2px;
  }
  .brand-tag {
    font-weight: 700; font-style: italic; font-size: 15px; color: var(--ink); margin-top: 1px;
  }
  .hero-photo {
    position: absolute; left: 0; top: 63px; width: 335px; height: 197px;
    background: linear-gradient(120deg, var(--photo-a) 0%, #dfe4e0 45%, var(--photo-b) 100%);
    border-bottom: 3px solid var(--blue-deep);
  }
  .generation {
    position: absolute; left: 17px; top: 268px; width: 310px;
  }
  .generation h2 {
    font-family: "Roboto Condensed", sans-serif; font-weight: 400;
    font-size: 26px; color: var(--ink); line-height: 1; letter-spacing: -.3px;
  }
  .generation .sub {
    margin-top: 6px; font-family: "Roboto Condensed", sans-serif;
    font-size: 12.5px; line-height: 14px; color: var(--blue-deep); text-transform: uppercase;
  }
  .questions { list-style: none; margin-top: 12px; }
  .questions li {
    position: relative; padding-left: 16px; margin-bottom: 7px;
    font-size: 10.5px; line-height: 14px; font-weight: 700; font-style: italic; color: var(--ink-soft);
  }
  .questions li::before, .ask li::before, .help-list li::before {
    content: ""; position: absolute; left: 0; top: 4px; width: 6px; height: 6px; border-radius: 50%;
  }
  .questions li::before { background: var(--blue-deep); }

  .front-right {
    position: absolute; left: 335px; top: 0; width: 322px; height: 467px; color: var(--white);
  }
  .quote {
    margin: 33px 16px 0 36px; font-size: 11px; line-height: 14px; position: relative;
  }
  .quote b { font-weight: 700; }
  .quote::before { content: "\201C"; position: absolute; left: -16px; top: -3px; font-size: 20px; font-weight: 900; }
  .quote .close { font-weight: 900; font-size: 14px; }
  .tab {
    position: absolute; right: 0; background: var(--white); color: var(--ink);
    font-weight: 700; font-size: 16px; padding: 2px 12px 3px 12px;
    border-radius: 12px 0 0 12px;
  }
  .tab-mission { top: 110px; width: 124px; }
  .tab-ask { top: 275px; width: 130px; }
  .mission {
    position: absolute; left: 18px; top: 142px; width: 287px;
    font-size: 11px; line-height: 13.5px; text-align: justify;
  }
  .ask {
    position: absolute; left: 16px; top: 309px; width: 296px; list-style: none;
  }
  .ask li {
    position: relative; padding-left: 17px; font-size: 9.3px; line-height: 12px; margin-bottom: 12px;
  }
  .ask li::before { background: var(--white); top: 3px; width: 5px; height: 5px; }

  .front-url {
    position: absolute; left: 0; bottom: 0; width: 657px; height: 42px;
    background: linear-gradient(90deg, var(--blue-light), var(--blue-pale) 70%, var(--blue-light));
    text-align: center; line-height: 40px; font-weight: 700; font-size: 13px;
    letter-spacing: 4.2px; color: var(--ink-soft);
  }

  /* ---------- Back ---------- */
  .card-back { top: 620px; background: var(--white); }
  .back-left {
    position: absolute; left: 0; top: 0; width: 362px; height: 509px;
    background: linear-gradient(165deg, var(--blue-mid) 0%, var(--blue-deep) 55%, #0b5fb3 100%);
    color: var(--white);
  }
  .back-divider {
    position: absolute; left: 362px; top: 0; width: 13px; height: 509px;
    background: linear-gradient(90deg, var(--blue-pale), var(--blue-light));
    border-right: 1px solid var(--blue-mid);
  }
  .help-tab {
    position: absolute; left: 0; top: 23px; width: 215px; height: 27px;
    background: var(--white); color: var(--ink); border-radius: 0 14px 14px 0;
    font-weight: 700; font-size: 17px; line-height: 27px; padding-left: 19px;
  }
  .help-section h3 {
    font-weight: 700; font-style: italic; font-size: 14px; margin-bottom: 5px;
  }
  .help-list { list-style: none; }
  .help-list li {
    position: relative; padding-left: 17px; font-size: 12.5px; line-height: 16px; margin-bottom: 4px;
  }
  .help-list li::before { background: var(--white); top: 5px; }
  .help-consult { position: absolute; left: 20px; top: 62px; width: 320px; }
  .help-audit { position: absolute; left: 17px; top: 214px; width: 330px; }
  .help-audit .help-list li, .help-roadmap .help-list li { padding-left: 21px; }
  .help-audit .help-list li::before, .help-roadmap .help-list li::before { left: 3px; }
  .help-roadmap { position: absolute; left: 20px; top: 334px; width: 330px; }

  .back-contact {
    position: absolute; left: 0; top: 426px; width: 362px; height: 83px;
    background: linear-gradient(90deg, var(--blue-light), var(--blue-pale));
  }
  .contact-tab {
    position: absolute; left: 122px; top: -8px; width: 107px; height: 26px;
    background: #111; color: var(--white); font-weight: 700; font-size: 14px;
    text-align: center; line-height: 26px;
  }
  .phone {
    position: absolute; left: 0; top: 27px; width: 150px; height: 28px;
    background: var(--white); border-radius: 0 14px 14px 0;
    display: flex; align-items: center; padding-left: 20px; gap: 8px;
    font-weight: 700; font-size: 15px; color: var(--ink);
  }
  .back-brand { position: absolute; left: 177px; top: 26px; width: 180px; }
  .back-brand .brand-name { font-size: 12.5px; display: block; }
  .back-brand .rule { height: 1px; background: var(--blue-deep); margin: 3px 0 2px; width: 160px; }
  .back-brand .url { font-size: 10px; color: var(--ink-soft); }

  .stamp {
    position: absolute; left: 551px; top: 38px; width: 87px; height: 102px;
    border: 1px solid #333;
  }
  .address-line {
    position: absolute; left: 407px; width: 234px; height: 1px; background: #444;
  }
</style>
</head>
<body>

<section class="card card-front" aria-label="Postcard front">
  <div class="front-topband"></div>
  <div class="front-left">
    <div class="brand">
      <div class="brand-name">Hearthside Living Partners</div>
      <div class="brand-tag">Because you deserve it!</div>
    </div>
  </div>
  <div class="hero-photo" style="top:88px" role="img" aria-label="Photo of a smiling senior couple standing in front of their house"></div>
  <div class="generation" style="top:295px">
    <h2>As the 55+ generation ages</h2>
    <p class="sub">They have many important questions to consider,<br>but maybe none more important than these</p>
    <ul class="questions">
      <li>Once our physical abilities make living in our home, as it is today, a struggle, what are we going to do?</li>
      <li>Are we planning to move into an assisted living facility when our health declines? What will that cost?</li>
      <li>Are there any other viable options?</li>
    </ul>
  </div>

  <div class="front-right">
    <p class="quote"><b>Aging in place</b> has become the preferred lifestyle and a lower cost alternative to institutionalization. Experts expect home modifications, increased connectivity and improved healthcare will make this the obvious lifestyle choice <span class="close">&rdquo;</span></p>
    <div class="tab tab-mission">Our Mission</div>
    <p class="mission">Our mission is to help our client’s to continue living in their own homes safely, independently, and comfortably as they age. Our team is comprised of Certified Aging in Place specialists, Universal Design Consultants, Registered Nurses and Certified Home Inspectors. We utilize our skills and training to assess, design and optimize our client’s homes to handle whatever physical challenges the future may bring, allowing them to remain where they want to be as they age…..at home!</p>
    <div class="tab tab-ask">Ask yourself…</div>
    <ul class="ask">
      <li>Is your home functioning safely and efficiently? How do you know?</li>
      <li>Is your home well suited for the physical challenges that may come with natural aging or an unfortunate diagnosis?</li>
      <li>Are you aware there are many simple, cost effective and attractive ways to modify your home to make it fit your needs now and in the future?</li>
      <li>Are you aware there are many new technology products that can help make your home safe, functional and more enjoyable?</li>
    </ul>
  </div>

  <div class="front-url">www.hearthsidelivingpartners.com</div>
</section>

<section class="card card-back" aria-label="Postcard back">
  <div class="back-left">
    <div class="help-tab">Here’s how we can help..</div>

    <div class="help-section help-consult">
      <h3>Free 30 minute in-home consultation</h3>
      <ul class="help-list">
        <li>Registers you for free access to our network of pre-screened and senior friendly contractors and service providers</li>
        <li>Contractor fraud education literature made available for those who wish to DIY.</li>
        <li>Cost comparison between investing in your home vs. cost of an assisted living facility.</li>
      </ul>
    </div>

    <div class="help-section help-audit">
      <h3>Home Audit</h3>
      <ul class="help-list">
        <li>Perform a comprehensive home inspection by certified inspector to assess the safety and functionality of your home.</li>
        <li>Identify what, if anything, needs to be addresses and refer the best contractor for the job.</li>
      </ul>
    </div>

    <div class="help-section help-roadmap">
      <h3>Aging in place consultation:</h3>
      <ul class="help-list">
        <li>Produce a written “road map” identifying improvements that can be done to proactively address your physical needs now and in the future.</li>
      </ul>
    </div>

    <div class="back-contact">
      <div class="contact-tab">Contact Us</div>
      <div class="phone">
        <svg width="14" height="14" viewBox="0 0 24 24" aria-hidden="true"><path fill="#1c1c1c" d="M6.6 10.8a15.1 15.1 0 0 0 6.6 6.6l2.2-2.2c.3-.3.7-.4 1-.2 1.1.4 2.3.6 3.6.6.6 0 1 .4 1 1V20c0 .6-.4 1-1 1A17 17 0 0 1 3 4c0-.6.4-1 1-1h3.5c.6 0 1 .4 1 1 0 1.3.2 2.5.6 3.6.1.3 0 .7-.2 1z"/></svg>
        0161 555 0142
      </div>
      <div class="back-brand">
        <span class="brand-name">Hearthside Living Partners</span>
        <div class="rule"></div>
        <div class="url">www.hearthsidelivingpartners.com</div>
      </div>
    </div>
  </div>
  <div class="back-divider"></div>

  <div class="stamp" aria-label="Stamp box"></div>
  <div class="address-line" style="top:244px"></div>
  <div class="address-line" style="top:285px"></div>
  <div class="address-line" style="top:318px"></div>
</section>

</body>
</html>
```